The Morrow Ledgers Website

I need a website to help promote the series of science fiction novels that I am in the process of writing.

I have some content and photos and am in the process of getting some new book cover artwork designed.

I have a current website/domain etc http://www.vantorpagehouse.co.nz but I need something a little more professional and eye catchig but I also want to be able to manage the content myself.

I can send e-versions of the two completed novels for context to any takers

```html
<!DOCTYPE html>
<html lang="en">
<head>
<meta charset="utf-8">
<title>The Morrow Ledgers</title>
<link rel="stylesheet" href="https://fonts.googleapis.com/css2?family=Tinos&family=Arimo:wght@400;700&family=Open+Sans:wght@400;600;700&display=swap">
<style>
:root{
  --brand:#1a7fa6;
  --link:#1a6fa8;
  --ink:#444;
  --head:#666;
  --muted:#888;
  --soft:#999;
  --rule:#cfcfcf;
  --panel:#efefef;
  --hero-light:#6bbde3;
  --hero-mid:#2f86c4;
  --hero-dark:#083d78;
  --cover-top:#3a3a3a;
  --cover-bottom:#111;
  --white:#fff;
}
*{margin:0;padding:0;box-sizing:border-box}
html,body{width:1200px;height:1051px;overflow:hidden;background:var(--white)}
body{position:relative;font-family:"Arimo",Arial,sans-serif;color:var(--ink)}
.abs{position:absolute}
.site-title{left:0;width:1200px;top:30px;text-align:center;font-family:"Tinos","Times New Roman",serif;font-size:39px;color:var(--brand);font-weight:400}
.byline{left:0;width:1200px;top:81px;text-align:center;font-size:12.5px;color:var(--brand);letter-spacing:.3px}
.byline-rule{top:91px;height:1px;width:116px;background:var(--brand)}
.main-nav{top:121px;left:0;width:1200px;display:flex;justify-content:center;font-size:10.5px}
.main-nav a{color:var(--ink);text-decoration:none;margin:0 10px}
.main-nav a.active{color:var(--brand)}
.hero{top:153px;left:0;width:1200px;height:252px;background:radial-gradient(ellipse 420px 220px at 640px 90px,var(--hero-light) 0%,var(--hero-mid) 55%,var(--hero-dark) 100%)}
.cover{background:linear-gradient(180deg,var(--cover-top),var(--cover-bottom));border-right:4px solid #d8d8d8;box-shadow:3px 3px 4px rgba(0,0,0,.35)}
.hero-copy{left:577px;top:259px;width:270px;font-size:16px;line-height:22px;color:var(--white)}
.intro{left:486px;top:447px;width:425px;font-size:7.8px;line-height:11px;color:var(--ink)}
.intro p{margin-bottom:7px}
.learn-more{left:486px;top:630px;font-size:6.5px;color:var(--muted);text-decoration:underline;letter-spacing:.3px}
.rule{height:1px;background:var(--rule)}
.section-head{font-size:11px;font-weight:400;color:var(--head)}
.blog-panel{left:298px;top:707px;width:282px;height:81px;background:var(--panel)}
.blog-panel::after{content:"";position:absolute;left:18px;bottom:-8px;border-left:7px solid transparent;border-right:7px solid transparent;border-top:8px solid var(--panel)}
.blog-title{left:306px;top:724px;width:270px;font-size:8.6px;color:var(--ink);white-space:nowrap}
.blog-text{left:310px;top:745px;width:255px;font-size:7.8px;line-height:11px;color:var(--muted)}
.more{color:var(--link)}
.blog-meta{left:300px;top:800px;font-size:8px;color:var(--muted);font-weight:700}
.blog-meta em{font-weight:400;font-size:7px;margin-left:6px;color:var(--soft)}
.review-title{left:621px;top:709px;font-size:8px;font-weight:700;color:#555}
.review-title span{color:var(--link);margin-left:4px}
.review-text{left:619px;top:736px;width:285px;font-size:7.8px;line-height:11px;color:var(--muted)}
.foot-title{left:298px;top:856px;font-family:"Tinos","Times New Roman",serif;font-size:15px;color:#777}
.foot-byline{left:300px;top:878px;font-size:9px;color:var(--brand);letter-spacing:.3px}
.foot-email{left:298px;top:906px;font-family:"Open Sans",Arial,sans-serif;font-size:6.5px;color:var(--soft)}
.col-head{font-family:"Open Sans",Arial,sans-serif;font-size:8px;font-weight:700;color:#666}
.tweet{left:497px;width:215px;font-family:"Open Sans",Arial,sans-serif;font-size:7.3px;line-height:10.5px;color:var(--soft)}
.tweet .handle{color:var(--link);font-size:8px}
.tweet small{display:block;font-size:5.5px;color:var(--soft)}
.recent{left:764px;width:134px;font-family:"Open Sans",Arial,sans-serif;font-size:7.3px;color:var(--muted);list-style:none}
.recent li{height:24.5px;padding-top:3px;border-bottom:1px solid #e2e2e2}
.recent li:first-child{color:var(--link)}
.recent li:last-child{border-bottom:none}
.copyright{left:298px;top:1023px;font-family:"Open Sans",Arial,sans-serif;font-size:6px;color:var(--muted)}
.social{top:1021px;width:11px;height:11px;border-radius:50%;background:#9a9a9a}
</style>
</head>
<body>
<header>
  <h1 class="abs site-title">The Morrow Ledgers</h1>
  <div class="abs byline-rule" style="left:401px"></div>
  <p class="abs byline">AUTHOR : WARREN HALE</p>
  <div class="abs byline-rule" style="left:685px"></div>
  <nav class="abs main-nav">
    <a class="active" href="#">Home</a><a href="#">Reviews</a><a href="#">About Us</a><a href="#">Blogs</a><a href="#">Contact Us</a><a href="#">Links</a>
  </nav>
</header>

<section class="abs hero"></section>
<div class="abs cover" role="img" aria-label="Book cover artwork for The Second Tide, large" style="left:371px;top:184px;width:119px;height:189px"></div>
<div class="abs cover" role="img" aria-label="Book cover artwork for The Second Tide, small" style="left:489px;top:250px;width:60px;height:128px"></div>
<p class="abs hero-copy">The Morrow Ledgers come to Warren's scifi page where you can find links to his scifi novels.</p>

<div class="abs cover" role="img" aria-label="Book cover artwork for The Second Tide" style="left:298px;top:447px;width:108px;height:173px"></div>
<div class="abs intro">
  <p>The Morrow Ledgers come to Warren's scifi page where you can find links to his scifi novels: Morrow - The First Ledger and the recently published The Second Tide.</p>
  <p>Morrow is the first novel in the Morrow series and the Second Tide is part two of the trilogy.</p>
  <p>This site is all about unashamed self promotion of Warren's novels</p>
  <p style="margin-top:12px;margin-bottom:0">The Second Tide</p>
  <p>Welcome to Morrow – the most technically sophisticated and powerful civilization in the known universe.</p>
  <p style="margin-top:27px">The Second Tide is the second novel in the Morrow Ledgers series and follows on from the first novel where our unlikely protagonists were kidnapped by a desperate food research team from the Planet Morrow. The researchers were on a mission to locate expertise to assist them in developing organic food sources to feed their people as their planet's synthetic food production systems had begun to fail for some inexplicable reason.</p>
</div>
<a class="abs learn-more" href="#">LEARN MORE &gt;&gt;</a>

<div class="abs rule" style="left:298px;top:654px;width:601px"></div>

<h2 class="abs section-head" style="left:298px;top:676px">Blogs</h2>
<div class="abs rule" style="left:333px;top:683px;width:247px"></div>
<div class="abs blog-panel"></div>
<p class="abs blog-title">- Civic Union Party struggles for a clear purpose in the modern world</p>
<p class="abs blog-text">This week Prime Minister Alan Pryor announced the date of the next election. Predictably the Civic Union Party led by David Renner came out swinging <span class="more">[.....]</span></p>
<p class="abs blog-meta">Author Warren, <em>Friday, 14 March 2014</em></p>

<h2 class="abs section-head" style="left:619px;top:676px">Reviews for the Morrow Ledger</h2>
<div class="abs rule" style="left:787px;top:683px;width:112px"></div>
<p class="abs review-title">Unpolished, But Still a Gem <span>By Martin Coles</span></p>
<p class="abs review-text">The Second Tide by Warren Hale is a next-in-series title about several different people whose stories are in some way related, but if you are just coming in you don't quite know how. Sue and Bruce are normal, everyday Earthlings... mostly. Sue, who owns a travel agency, is somehow pregnant when she hasn't had a sexual partner in a very long time. <span class="more">[.....]</span></p>

<div class="abs rule" style="left:298px;top:837px;width:601px"></div>

<footer>
  <p class="abs foot-title">The Morrow Ledgers</p>
  <p class="abs foot-byline">AUTHOR : WARREN HALE</p>
  <p class="abs foot-email"><b>Email:</b> hello@vantorpagehouse.co.nz</p>

  <h3 class="abs col-head" style="left:497px;top:862px">GET IN TWEET</h3>
  <div class="abs tweet" style="top:890px"><span class="handle">@morrowledgers</span> Lorem Ipsum is simply dummy text of the printing and typesetting industry<small>5 min ago</small></div>
  <div class="abs rule" style="left:497px;top:933px;width:198px;background:#e0e0e0"></div>
  <div class="abs tweet" style="top:944px"><span class="handle">@morrowledgers</span> Lorem Ipsum is simply dummy text of the printing and typesetting industry<small>5 min ago</small></div>

  <h3 class="abs col-head" style="left:764px;top:862px">RECENT REVIEW</h3>
  <ul class="abs recent" style="top:889px">
    <li>Lorem Ipsum is simply dummy</li>
    <li>Lorem Ipsum is simply dummy</li>
    <li>Lorem Ipsum is simply dummy</li>
    <li>Lorem Ipsum is simply dummy</li>
  </ul>

  <div class="abs rule" style="left:298px;top:1005px;width:601px"></div>
  <p class="abs copyright">Copyright 2014 All Right Reserved Company Name</p>
  <span class="abs social" style="left:819px" aria-label="Social link"></span>
  <span class="abs social" style="left:841px" aria-label="Video link"></span>
  <span class="abs social" style="left:864px" aria-label="Social link"></span>
  <span class="abs social" style="left:887px" aria-label="Social link"></span>
</footer>
</body>
</html>
```